Complete redesign of Licensed Medical Cannabis Dispensary website

Redesign website to modernize it and simplify it and add a self service reservation/preorder interactive delivery form. Also integrate current POS system that has current inventory. Here is a website for inspiration that I really like because of it simplicity https://www.grovaleaf.example and easy ordering option. Attached is our logo.... please design around that and this is our website address www.mistrelcourierhouse.example

Font styles to use
Sans Serif

Colors
5c5c5c
cbcbcb
000000
add136

Requirements
Must have
• inventory thats integrated with pos
• online reservation/delivery form
Nice to have
• a website thats modern and simple
• The website designed are the logo that is attached
Should not have
• too much information

```html
<!DOCTYPE html>
<html lang="en">
<head>
<meta charset="utf-8">
<title>Mistrel Courier — Top Shelf Medical Marijuana Delivery</title>
<link rel="stylesheet" href="https://fonts.googleapis.com/css2?family=DM+Serif+Display&family=Raleway:wght@400;500;600;700&display=swap">
<style>
:root{
  --lime:#add136;
  --lime-dark:#97b82a;
  --ink:#000000;
  --grey:#5c5c5c;
  --silver:#cbcbcb;
  --slate:#25282c;
  --slate-deep:#1d1f22;
  --white:#ffffff;
  --serif:"DM Serif Display", Georgia, serif;
  --sans:"Raleway", Arial, sans-serif;
}
*{box-sizing:border-box;margin:0;padding:0}
html,body{width:1200px;height:3422px;overflow:hidden;background:var(--white)}
body{position:relative;font-family:var(--sans);color:var(--grey)}
.abs{position:absolute}

/* header */
.topbar{top:0;left:0;width:1200px;height:32px;font-size:11px;font-weight:600;color:var(--grey)}
.topbar .contact{left:230px;top:10px;display:flex;gap:12px;align-items:center}
.topbar .contact b{color:var(--lime)}
.topbar .reserve{left:723px;top:0;width:247px;height:32px;background:var(--lime);color:var(--white);font-size:10px;font-weight:700;display:flex;align-items:center;justify-content:center;letter-spacing:.5px}
.brand{left:230px;top:46px;display:flex;align-items:center;gap:10px}
.brand .mark{width:36px;height:36px;border-radius:50%;background:var(--lime)}
.brand .name{font-family:var(--serif);font-size:22px;color:var(--grey)}
.nav{top:52px;font-size:10px;font-weight:700;color:var(--grey);letter-spacing:.5px}
.nav.active{color:var(--lime)}
.btn-outline-sm{top:46px;height:32px;border:1px solid var(--silver);font-size:10px;font-weight:700;display:flex;align-items:center;justify-content:center;color:var(--grey)}

/* hero */
.hero{top:96px;left:0;width:1200px;height:502px;background:radial-gradient(ellipse at 30% 40%,#5d7a34 0%,#2f4a22 45%,#16240f 100%);clip-path:polygon(0 0,100% 0,100% 78%,50% 100%,0 78%)}
.hero-title{top:196px;left:0;width:1200px;text-align:center;font-family:var(--serif);font-size:78px;line-height:88px;color:var(--white)}
.hero-sub{top:384px;left:0;width:1200px;text-align:center;font-size:12px;font-weight:600;color:var(--white);letter-spacing:.5px}
.btn{display:flex;align-items:center;justify-content:center;font-size:10px;font-weight:700;letter-spacing:.5px}
.btn-lime{background:var(--lime);color:var(--white)}
.btn-white{background:var(--white);color:var(--grey)}

/* steps */
.step{top:664px;display:flex;align-items:center;gap:6px}
.step .dot{width:40px;height:40px;border-radius:50%;display:flex;align-items:center;justify-content:center;font-family:var(--serif);font-size:20px;color:var(--white);background:#4a4a4a}
.step .dot.done{background:var(--lime)}
.step-label{top:722px;font-family:var(--serif);font-size:19px;color:var(--silver)}
.step-label.current{color:var(--ink)}
.field{border-bottom:1px solid var(--silver);height:42px}
.field.filled{border-bottom:2px solid var(--grey)}
.field .hint{position:absolute;top:-2px;font-size:10px;color:var(--silver)}
.field .label{position:absolute;bottom:8px;font-size:13px;color:var(--grey)}

/* features */
.dark-band{left:0;width:1200px;background:linear-gradient(160deg,#2d3530 0%,#22282a 55%,#1e2224 100%)}
.features{top:1120px;height:322px;clip-path:polygon(0 0,100% 0,100% 70%,50% 100%,0 70%)}
.feature{top:1212px;width:220px;color:var(--white)}
.feature h3{font-family:var(--serif);font-weight:400;font-size:26px;margin:14px 0 10px}
.feature p{font-size:12px;line-height:19px;color:#d5d5d5}

/* cta */
.cta-text{font-family:var(--serif);font-size:20px;line-height:24px}
.cta-text sup{font-size:13px}
.rule{top:1667px;left:230px;width:740px;height:1px;background:var(--silver)}

/* products */
.section-title{font-family:var(--serif);font-size:38px;color:var(--grey);left:230px}
.card{width:176px;height:256px;border:1px solid var(--silver);background:var(--white)}
.card .photo{height:176px}
.card .pname{position:absolute;left:10px;top:190px;font-family:var(--serif);font-size:14px;color:var(--ink)}
.card .price{position:absolute;left:10px;top:216px;font-family:var(--serif);font-size:20px;color:var(--ink)}
.card .price sup{font-size:11px}
.card .cart{position:absolute;right:-1px;bottom:-1px;width:38px;height:38px;background:var(--lime);display:flex;align-items:center;justify-content:center}
.arrow{width:36px;height:114px;border:1px solid var(--silver);background:var(--white);display:flex;align-items:center;justify-content:center}

/* testimonials */
.testimonials{top:2144px;height:422px;clip-path:polygon(0 0,100% 0,100% 73%,50% 100%,0 73%)}
.quote{top:2316px;width:330px;font-size:12px;line-height:19px;font-style:italic;color:#e4e4e4}
.quote::before{content:"\201C";position:absolute;left:-2px;top:-14px;font-size:22px;font-style:normal;color:var(--white)}
.author{top:2380px;display:flex;align-items:center;gap:16px;color:var(--white);font-size:13px;font-weight:700}
.avatar{width:54px;height:54px;border-radius:50%;border:3px solid var(--white)}

/* green band */
.green-band{top:3011px;left:0;width:1200px;height:123px;background:var(--lime)}

/* footer */
.footer{top:3134px;left:0;width:1200px;height:246px;background:var(--slate)}
.footer h4{font-family:var(--serif);font-weight:400;font-size:15px;color:var(--white)}
.footer li{list-style:none;font-size:10px;color:#cfcfcf;display:flex;align-items:center;gap:10px;margin-bottom:12px}
.footer li::before{content:"";width:5px;height:5px;border-radius:50%;background:var(--lime)}
.f-testi{display:flex;gap:10px;font-size:9px;line-height:13px;color:#cfcfcf;width:200px;margin-bottom:14px}
.f-testi .mini{width:30px;height:30px;border-radius:50%;flex:none}
.f-contact{display:flex;gap:14px;align-items:center;font-size:9px;color:#cfcfcf;margin-bottom:18px}
.copyright{top:3380px;left:0;width:1200px;height:42px;background:var(--slate-deep);color:#cfcfcf;font-size:9px;font-weight:600;display:flex;align-items:center;justify-content:center;letter-spacing:.5px}
</style>
</head>
<body>

<!-- header -->
<div class="abs topbar">
  <div class="abs contact"><span><b>✆</b> ORDER: 510-555-0142</span><span>|</span><span><b>✉</b> hello@mistrelcourierhouse.example</span></div>
  <div class="abs reserve">SELF SERVICE RESERVATION / PREORDER</div>
</div>
<div class="abs brand"><span class="mark"></span><span class="name">Mistrel Courier</span></div>
<div class="abs nav active" style="left:493px">HOME</div>
<div class="abs nav" style="left:556px">FORUMS</div>
<div class="abs nav" style="left:626px">STORE</div>
<div class="abs nav" style="left:686px">CONTACT US</div>
<div class="abs nav" style="left:803px">LOGIN</div>
<div class="abs btn-outline-sm" style="left:844px;width:52px">SIGN UP</div>
<svg class="abs" style="left:915px;top:54px" width="16" height="16" viewBox="0 0 16 16"><circle cx="6.5" cy="6.5" r="4.5" fill="none" stroke="#5c5c5c" stroke-width="1.6"/><line x1="10" y1="10" x2="14" y2="14" stroke="#5c5c5c" stroke-width="1.6"/></svg>
<div class="abs btn-outline-sm" style="left:938px;width:32px">
  <svg width="14" height="12" viewBox="0 0 14 12"><path d="M0 1h2.5l2 7h7l1.5-5H4" fill="none" stroke="#5c5c5c" stroke-width="1.3"/><circle cx="5.5" cy="10.5" r="1" fill="#5c5c5c"/><circle cx="10.5" cy="10.5" r="1" fill="#5c5c5c"/></svg>
</div>

<!-- hero -->
<div class="abs hero" role="img" aria-label="Close-up photograph of cannabis plant leaves in green light"></div>
<h1 class="abs hero-title" style="font-weight:400">Top Shelf Medical<br>Marijuana Delivery</h1>
<p class="abs hero-sub">WE OFFER ONLY THE HIGHEST QUALITY FLOWERS, EDIBLES AND CONCENTRATES.</p>
<div class="abs btn btn-lime" style="left:456px;top:438px;width:132px;height:34px">SHOP NOW</div>
<div class="abs btn btn-white" style="left:609px;top:438px;width:132px;height:34px">GET VERIFIED</div>

<!-- order steps -->
<div class="abs step" style="left:230px"><span class="dot done"><svg width="18" height="14" viewBox="0 0 18 14"><path d="M1 7l5 5L17 1" fill="none" stroke="#fff" stroke-width="2.4"/></svg></span>
  <svg width="62" height="10" viewBox="0 0 62 10"><line x1="0" y1="5" x2="60" y2="5" stroke="#cbcbcb"/><path d="M55 1l5 4-5 4" fill="none" stroke="#cbcbcb"/></svg></div>
<div class="abs step" style="left:484px"><span class="dot">2</span>
  <svg width="62" height="10" viewBox="0 0 62 10"><line x1="0" y1="5" x2="60" y2="5" stroke="#cbcbcb"/><path d="M55 1l5 4-5 4" fill="none" stroke="#cbcbcb"/></svg></div>
<div class="abs step" style="left:732px"><span class="dot">3</span>
  <svg width="62" height="10" viewBox="0 0 62 10"><line x1="0" y1="5" x2="60" y2="5" stroke="#cbcbcb"/><path d="M55 1l5 4-5 4" fill="none" stroke="#cbcbcb"/></svg></div>
<div class="abs step-label current" style="left:230px">Basic Information</div>
<div class="abs step-label" style="left:481px">Delivery &amp; Payment</div>
<div class="abs step-label" style="left:732px">Complete Order</div>

<div class="abs field filled" style="left:230px;top:800px;width:302px"><span class="hint">First Name</span><span class="label">Gerlin</span></div>
<div class="abs field" style="left:604px;top:800px;width:366px"><span class="label">Last Name</span></div>
<div class="abs field" style="left:230px;top:870px;width:302px"><span class="label">Email</span></div>
<div class="abs field" style="left:604px;top:870px;width:366px"><span class="label">Phone</span></div>
<div class="abs field" style="left:230px;top:941px;width:740px"><span class="label">Address</span></div>
<div class="abs btn btn-lime" style="left:837px;top:1020px;width:133px;height:34px">NEXT</div>

<!-- how it works -->
<div class="abs dark-band features" role="img" aria-label="Dark photograph of cannabis leaves"></div>
<div class="abs feature" style="left:267px">
  <svg width="38" height="42" viewBox="0 0 38 42"><rect x="4" y="5" width="28" height="35" rx="3" fill="none" stroke="#fff" stroke-width="2"/><rect x="12" y="1" width="12" height="7" rx="2" fill="none" stroke="#fff" stroke-width="2"/><path d="M10 17l2 2 4-4M10 26l2 2 4-4" fill="none" stroke="#fff" stroke-width="1.6"/><line x1="19" y1="17" x2="27" y2="17" stroke="#fff" stroke-width="1.6"/><line x1="19" y1="26" x2="27" y2="26" stroke="#fff" stroke-width="1.6"/></svg>
  <h3>Get Verified</h3><p>It's fast. It's simple. Just fill out our verification form and get approved in minutes.</p></div>
<div class="abs feature" style="left:515px">
  <svg width="48" height="42" viewBox="0 0 48 42"><path d="M1 4h7l5 22h26l5-16H11" fill="none" stroke="#fff" stroke-width="2.2"/><circle cx="17" cy="35" r="3.5" fill="none" stroke="#fff" stroke-width="2"/><circle cx="35" cy="35" r="3.5" fill="none" stroke="#fff" stroke-width="2"/></svg>
  <h3>Shop</h3><p>Add the products you want to your shopping cart and check-out. No credit card required!</p></div>
<div class="abs feature" style="left:764px">
  <svg width="42" height="42" viewBox="0 0 42 42"><circle cx="21" cy="21" r="19" fill="none" stroke="#fff" stroke-width="2.2"/><path d="M12 21l6 6 12-12" fill="none" stroke="#fff" stroke-width="2.4"/></svg>
  <h3>Get Medicated</h3><p>Sit back and wait. Our professional staff will deliver your medication right to your front door.</p></div>

<!-- recommendation cta -->
<div class="abs cta-text" style="left:230px;top:1570px;color:var(--ink)">Don't have your doctor's recommendation yet?<br>Get it online for just <sup>$</sup>49<sup>00</sup></div>
<div class="abs btn btn-lime" style="left:837px;top:1583px;width:133px;height:36px">GET STARTED</div>
<div class="abs rule"></div>

<!-- flowers -->
<h2 class="abs section-title" style="top:1720px;font-weight:400">Flowers</h2>
<div class="abs arrow" style="left:160px;top:1861px"><svg width="12" height="60" viewBox="0 0 12 60"><path d="M11 1L1 30l10 29" fill="none" stroke="#5c5c5c"/></svg></div>
<div class="abs arrow" style="left:1004px;top:1861px"><svg width="12" height="60" viewBox="0 0 12 60"><path d="M1 1l10 29L1 59" fill="none" stroke="#5c5c5c"/></svg></div>

<div class="abs card" style="left:230px;top:1790px"><div class="photo" role="img" aria-label="Photo of Super Glue cannabis buds" style="background:linear-gradient(135deg,#8fa36a,#5f7347)"></div><span class="pname">Super Glue</span><span class="price"><sup>$</sup>30<sup>00</sup></span><span class="cart"><svg width="16" height="14" viewBox="0 0 16 14"><path d="M2 5h12l-2 8H4z" fill="#fff"/><path d="M5 5l3-4 3 4" fill="none" stroke="#fff" stroke-width="1.4"/></svg></span></div>
<div class="abs card" style="left:418px;top:1790px"><div class="photo" role="img" aria-label="Photo of Candyland cannabis buds" style="background:linear-gradient(135deg,#7d6a4d,#4e4232)"></div><span class="pname">Candyland</span><span class="price"><sup>$</sup>15<sup>00</sup> – <sup>$</sup>30<sup>00</sup></span><span class="cart"><svg width="16" height="14" viewBox="0 0 16 14"><path d="M2 5h12l-2 8H4z" fill="#fff"/><path d="M5 5l3-4 3 4" fill="none" stroke="#fff" stroke-width="1.4"/></svg></span></div>
<div class="abs card" style="left:606px;top:1790px"><div class="photo" role="img" aria-label="Photo of Sour Diesel cannabis buds" style="background:linear-gradient(135deg,#9aa35a,#6d7a3c)"></div><span class="pname">Sour Diesel</span><span class="price"><sup>$</sup>35<sup>00</sup></span><span class="cart"><svg width="16" height="14" viewBox="0 0 16 14"><path d="M2 5h12l-2 8H4z" fill="#fff"/><path d="M5 5l3-4 3 4" fill="none" stroke="#fff" stroke-width="1.4"/></svg></span></div>
<div class="abs card" style="left:794px;top:1790px"><div class="photo" role="img" aria-label="Photo of Berry Bright cannabis buds" style="background:linear-gradient(135deg,#6b7a52,#3a4230)"></div><span class="pname">Berry Bright</span><span class="price"><sup>$</sup>15<sup>00</sup> – <sup>$</sup>30<sup>00</sup></span><span class="cart"><svg width="16" height="14" viewBox="0 0 16 14"><path d="M2 5h12l-2 8H4z" fill="#fff"/><path d="M5 5l3-4 3 4" fill="none" stroke="#fff" stroke-width="1.4"/></svg></span></div>

<!-- testimonials -->
<div class="abs dark-band testimonials" role="img" aria-label="Dark photograph of a cannabis grow field"></div>
<h2 class="abs section-title" style="top:2216px;color:var(--white);font-weight:400">Client Testimonials</h2>
<p class="abs quote" style="left:236px">These guys really know their stuff man. Nothin' but the kind here!</p>
<p class="abs quote" style="left:612px">This dispensary has the very best med! I love their sour diesel!</p>
<div class="abs author" style="left:230px"><span class="avatar" role="img" aria-label="Portrait of client John G." style="background:#6b5a4c"></span>John G.</div>
<div class="abs author" style="left:606px"><span class="avatar" role="img" aria-label="Portrait of client Jane D." style="background:#b08a78"></span>Jane D.</div>

<!-- concentrate -->
<h2 class="abs section-title" style="top:2618px;font-weight:400;font-size:34px;letter-spacing:1px">CONCENTRATE</h2>
<div class="abs arrow" style="left:160px;top:2758px"><svg width="12" height="60" viewBox="0 0 12 60"><path d="M11 1L1 30l10 29" fill="none" stroke="#5c5c5c"/></svg></div>
<div class="abs arrow" style="left:1004px;top:2758px"><svg width="12" height="60" viewBox="0 0 12 60"><path d="M1 1l10 29L1 59" fill="none" stroke="#5c5c5c"/></svg></div>

<div class="abs card" style="left:230px;top:2691px"><div class="photo" role="img" aria-label="Photo of Citrus Sap Shatter concentrate" style="background:linear-gradient(135deg,#d2cbbd,#8c7658)"></div><span class="pname">Citrus Sap Shatter</span><span class="price"><sup>$</sup>25<sup>00</sup></span><span class="cart"><svg width="16" height="14" viewBox="0 0 16 14"><path d="M2 5h12l-2 8H4z" fill="#fff"/><path d="M5 5l3-4 3 4" fill="none" stroke="#fff" stroke-width="1.4"/></svg></span></div>
<div class="abs card" style="left:418px;top:2691px"><div class="photo" role="img" aria-label="Photo of a GG #1 vape cartridge" style="background:linear-gradient(135deg,#6a655c,#2c2a27)"></div><span class="pname">GG #1 CART</span><span class="price"><sup>$</sup>30<sup>00</sup></span><span class="cart"><svg width="16" height="14" viewBox="0 0 16 14"><path d="M2 5h12l-2 8H4z" fill="#fff"/><path d="M5 5l3-4 3 4" fill="none" stroke="#fff" stroke-width="1.4"/></svg></span></div>
<div class="abs card" style="left:606px;top:2691px"><div class="photo" role="img" aria-label="Photo of Zestel vape cartridges" style="background:linear-gradient(135deg,#3a3d32,#8a8b3c)"></div><span class="pname">Zestel Cart.</span><span class="price"><sup>$</sup>30<sup>00</sup></span><span class="cart"><svg width="16" height="14" viewBox="0 0 16 14"><path d="M2 5h12l-2 8H4z" fill="#fff"/><path d="M5 5l3-4 3 4" fill="none" stroke="#fff" stroke-width="1.4"/></svg></span></div>
<div class="abs card" style="left:794px;top:2691px"><div class="photo" role="img" aria-label="Photo of Pink Prowler vape cartridges" style="background:linear-gradient(135deg,#3a3d32,#9a9a3e)"></div><span class="pname">Pink Prowler Cart.</span><span class="price"><sup>$</sup>30<sup>00</sup></span><span class="cart"><svg width="16" height="14" viewBox="0 0 16 14"><path d="M2 5h12l-2 8H4z" fill="#fff"/><path d="M5 5l3-4 3 4" fill="none" stroke="#fff" stroke-width="1.4"/></svg></span></div>

<!-- green cta band -->
<div class="abs green-band"></div>
<div class="abs cta-text" style="left:230px;top:3045px;color:var(--white)">Don't have your doctor's recommendation yet?<br>Get it online for just <sup>$</sup>49<sup>00</sup></div>
<div class="abs btn btn-white" style="left:837px;top:3055px;width:133px;height:36px">GET STARTED</div>

<!-- footer -->
<div class="abs footer"></div>
<div class="abs" style="left:230px;top:3196px;display:flex;align-items:center;gap:10px"><span style="width:40px;height:40px;border-radius:50%;background:var(--lime)"></span><span style="font-family:var(--serif);font-size:17px;color:var(--white)">Mistrel Courier</span></div>
<div class="abs" style="left:406px;top:3186px"><h4>Quick Links</h4><ul style="margin-top:22px"><li>Home</li><li>Forums</li><li>store</li><li>contact us</li></ul></div>
<div class="abs" style="left:543px;top:3186px"><h4>Testimonial</h4>
  <div style="margin-top:20px">
    <div class="f-testi"><span class="mini" role="img" aria-label="Portrait of client Jane D." style="background:#b08a78"></span><span>"This dispensary has the very best med! I love their sour diesel!"<br><br>Jane D.</span></div>
    <div class="f-testi"><span class="mini" role="img" aria-label="Portrait of client John G." style="background:#6b5a4c"></span><span>"These guys really know their stuff man. Nothin' but the kind here!"<br><br>John G.</span></div>
  </div></div>
<div class="abs" style="left:789px;top:3186px"><h4>Contact Us</h4>
  <div style="margin-top:22px">
    <div class="f-contact"><svg width="14" height="14" viewBox="0 0 14 14"><path d="M3 1l2.5 3-1.5 1.5c1 2 2.5 3.5 4.5 4.5L10 8.5l3 2.5-1.5 2C6 13 1 8 1 2.5z" fill="#add136"/></svg>555-555-5555</div>
    <div class="f-contact"><svg width="14" height="12" viewBox="0 0 14 12"><rect x="1" y="1" width="12" height="10" fill="none" stroke="#add136" stroke-width="1.4"/><path d="M1 1l6 5 6-5" fill="none" stroke="#add136" stroke-width="1.4"/></svg>hello@mistrelcourierhouse.example</div>
    <div class="f-contact"><svg width="12" height="16" viewBox="0 0 12 16"><path d="M6 15S1 9 1 6a5 5 0 0110 0c0 3-5 9-5 9z" fill="#add136"/><circle cx="6" cy="6" r="2" fill="#25282c"/></svg>12 Orchard Lane</div>
  </div></div>
<div class="abs copyright">© 2018 MISTREL COURIER HOUSE. ALL RIGHTS RESERVED.</div>

</body>
</html>
```